Business card design for Bront Engineering Qavo

We need a new business card design along with all the necessary to place an order. The company is Bront Engineering Qavo and we recently updated our logo.

```html
<!DOCTYPE html>
<html lang="en">
<head>
<meta charset="utf-8">
<title>Bront Engineering Qavo – Business Card</title>
<link href="https://fonts.googleapis.com/css2?family=Outfit:wght@400;500;600&display=swap" rel="stylesheet">
<style>
  :root {
    --page: #ffffff;
    --card: #1b1b1b;
    --grey: #9a9a9a;
    --yellow: #e2c024;
  }
  html, body {
    margin: 0;
    width: 1200px;
    height: 1200px;
    overflow: hidden;
    background: var(--page);
    font-family: "Outfit", sans-serif;
  }
  .canvas {
    position: relative;
    width: 1200px;
    height: 1200px;
  }
  .card {
    position: absolute;
    left: 208px;
    width: 751px;
    height: 441px;
    background: var(--card);
    border-radius: 26px;
    overflow: hidden;
  }
  .card-front { top: 181px; }
  .card-back { top: 648px; }

  .brand {
    position: absolute;
    display: flex;
    align-items: center;
    gap: 16px;
    color: var(--grey);
    font-weight: 600;
    letter-spacing: 0.04em;
    text-transform: uppercase;
    white-space: nowrap;
  }
  .brand-mark {
    width: 22px;
    height: 22px;
    background: var(--yellow);
    flex: none;
  }
  .card-front .brand {
    left: 0;
    right: 0;
    top: 190px;
    justify-content: center;
    font-size: 40px;
  }
  .card-back .brand {
    left: 28px;
    top: 70px;
    font-size: 30px;
    gap: 12px;
  }
  .card-back .brand-mark { width: 18px; height: 18px; }

  .person-name {
    position: absolute;
    left: 44px;
    top: 170px;
    margin: 0;
    font-size: 54px;
    font-weight: 600;
    color: var(--grey);
    letter-spacing: -0.01em;
    line-height: 1;
  }
  .person-role {
    position: absolute;
    left: 45px;
    top: 226px;
    margin: 0;
    font-size: 22px;
    font-weight: 500;
    color: var(--yellow);
  }
  .contact-list {
    position: absolute;
    left: 30px;
    top: 290px;
    margin: 0;
    padding: 0;
    list-style: none;
  }
  .contact {
    display: flex;
    align-items: center;
    color: var(--grey);
    font-weight: 600;
  }
  .contact svg { flex: none; fill: var(--yellow); }
  .contact-phone { font-size: 38px; gap: 14px; height: 48px; }
  .contact-mail, .contact-web { font-size: 20px; gap: 22px; height: 30px; margin-left: 3px; }
</style>
</head>
<body>
<main class="canvas">

  <section class="card card-front">
    <div class="brand"><span class="brand-mark"></span>Bront Engineering Qavo</div>
  </section>

  <section class="card card-back">
    <div class="brand"><span class="brand-mark"></span>Bront Engineering Qavo</div>

    <h1 class="person-name">Neil Garrow</h1>
    <p class="person-role">Deputy Production Manager</p>

    <ul class="contact-list">
      <li class="contact contact-phone">
        <svg width="30" height="30" viewBox="0 0 24 24" aria-hidden="true"><path d="M6.6 10.8c1.4 2.8 3.8 5.1 6.6 6.6l2.2-2.2c.3-.3.7-.4 1-.2 1.1.4 2.3.6 3.6.6.6 0 1 .4 1 1V20c0 .6-.4 1-1 1C10.6 21 3 13.4 3 4c0-.6.4-1 1-1h3.5c.6 0 1 .4 1 1 0 1.3.2 2.5.6 3.6.1.3 0 .7-.2 1z"/></svg>
        270 555 0148
      </li>
      <li class="contact contact-mail">
        <svg width="26" height="20" viewBox="0 0 26 20" aria-hidden="true"><path d="M0 0h26v20H0z M2 2v1l11 8 11-8V2z M2 5.5V18h22V5.5l-11 8z" fill-rule="evenodd"/></svg>
        ngarrow.bq@gmail.com
      </li>
      <li class="contact contact-web">
        <svg width="26" height="26" viewBox="0 0 24 24" aria-hidden="true"><path d="M12 2a10 10 0 1 0 0 20 10 10 0 0 0 0-20zm6.9 6h-3a15 15 0 0 0-1.3-3.9A8 8 0 0 1 18.9 8zM12 4c.8 1.2 1.5 2.5 1.9 4h-3.8c.4-1.5 1.1-2.8 1.9-4zM4.3 14a8 8 0 0 1 0-4h3.4a16 16 0 0 0 0 4zm.8 2h3a15 15 0 0 0 1.3 3.9A8 8 0 0 1 5.1 16zm3-8h-3a8 8 0 0 1 4.3-3.9A15 15 0 0 0 8.1 8zM12 20c-.8-1.2-1.5-2.5-1.9-4h3.8c-.4 1.5-1.1 2.8-1.9 4zm2.3-6H9.7a14 14 0 0 1 0-4h4.6a14 14 0 0 1 0 4zm.3 5.9a15 15 0 0 0 1.3-3.9h3a8 8 0 0 1-4.3 3.9zm1.7-5.9a16 16 0 0 0 0-4h3.4a8 8 0 0 1 0 4z"/></svg>
        brontengineeringqavo.com
      </li>
    </ul>
  </section>

</main>
</body>
</html>
```